Events floral designer business needs a logo design

I need a logo design for my floral design business called tender thistles.
i am inspired by nature and the simplicity of its beauty, whilst upcycling and recycling materials to reduce waste and impact on our environment.
I would like the design to be printed on recycled brown cardboard so i would like a simple but striking design of a bold black ivy vine or gnarly magnolia or tree branch with lower case old school type writer font.

Target Market(s)

Anyone requiring floral additions for their event

Industry/Entity Type

Business

Contact Information for Business Card

rosa kettering
floral designer/creator
0461807352
rosa@tenderthistles.com
tenderthistles.com

Font styles to use
Other font styles liked:
• lower case type writer

Colors
000000

Requirements
Must have
• simplicity but boldness
• Black typewriter font and bold picture with my details
Nice to have
• as above
Should not have
• colour

```html
<!DOCTYPE html>
<html lang="en">
<head>
<meta charset="utf-8">
<title>Rosa Kettering – Tender Thistles</title>
<link rel="stylesheet" href="https://fonts.googleapis.com/css2?family=Special+Elite&display=swap">
<style>
  :root {
    --paper: #ffffff;
    --ink: #000000;
    --artwork-light: #ececec;
    --artwork-mid: #cfcfcf;
    --artwork-dark: #8a8a8a;
  }
  html, body {
    margin: 0;
    padding: 0;
    overflow: hidden;
    background: var(--paper);
  }
  .card {
    position: relative;
    width: 685px;
    height: 1200px;
    background: var(--paper);
    color: var(--ink);
    font-family: "Special Elite", "Courier New", monospace;
    overflow: hidden;
  }
  .bloom-artwork {
    position: absolute;
    left: 62px;
    top: 141px;
    width: 561px;
    height: 440px;
    border-radius: 24px;
    background: linear-gradient(100deg, var(--artwork-dark) 0%, var(--artwork-mid) 30%, var(--artwork-light) 60%, var(--artwork-mid) 100%);
  }
  .details {
    position: absolute;
    left: 0;
    width: 100%;
    margin: 0;
    text-align: center;
    white-space: nowrap;
    line-height: 1;
  }
  .details--name {
    top: 732px;
    font-size: 36px;
    font-weight: 700;
  }
  .details--role {
    top: 781px;
    font-size: 35px;
    font-weight: 400;
  }
  .details--phone {
    top: 875px;
    font-size: 30px;
  }
  .details--email {
    top: 918px;
    font-size: 27px;
    font-weight: 700;
  }
  .details--website {
    top: 1099px;
    font-size: 31px;
    font-weight: 700;
  }
  .edge-rule {
    position: absolute;
    left: 0;
    bottom: 1px;
    width: 100%;
    height: 1px;
    background: var(--ink);
  }
</style>
</head>
<body>
  <main class="card">
    <div class="bloom-artwork" role="img" aria-label="Greyscale illustration of a white magnolia flower with dark leaves"></div>
    <h1 class="details details--name">ROSA KETTERING</h1>
    <p class="details details--role">FLORAL DESIGNER/ CREATOR</p>
    <p class="details details--phone">0461807352</p>
    <p class="details details--email">rosa@tenderthistles.com</p>
    <p class="details details--website">tenderthistles.com</p>
    <div class="edge-rule"></div>
  </main>
</body>
</html>
```